Design interface for an invoicing software

We are developing a new invoicing software that is a very boring topic. Users can use the software to write invoices and manage their income. Therefore we want to inspire the users with a great desgin. By this we mean, for example, the use of photos in the background (streets in New York, landscapes), or "crazy" looking headlines or something else. Target group are young start-ups, freelancers, hairdressers and taxi drivers at the age of 18-40 years. It would also be worth considering to adapt the look to the user's industry. However, the menu items themselves and the approximate position of the information are given. See file "startpoint" What kind of ideas do you have?

Target Market(s)

Europe

Industry/Entity Type

Small Business

Colors

Designer to choose colors to be used in the design.

Requirements
Must have
• the menu items themselves and the approximate position of the information are given. The navigation menu itself can be different.
Should not have
• boring look and feel

```html
<!DOCTYPE html>
<html lang="en">
<head>
<meta charset="utf-8">
<title>Invoicing Dashboard</title>
<link rel="stylesheet" href="https://fonts.googleapis.com/css2?family=Montserrat:wght@400;500;600;700;800;900&display=swap">
<style>
:root{
  --night-top:#2a1d57;
  --night-mid:#4a2a6e;
  --dusk:#8a5a7a;
  --ground:#2c2550;
  --sidebar:rgba(22,20,48,.78);
  --white:#ffffff;
  --magenta:#b012d8;
  --invoice-body:rgba(40,36,110,.88);
  --row-line:rgba(255,255,255,.14);
  --todo-top:#6a62d4;
  --todo-bottom:#5ae3a4;
  --todo-head:#8fe0c4;
  --stats-top:#e4862c;
  --stats-bottom:#c4561a;
  --pill:#b84a12;
  --muted-orange:#f3b27a;
  --search:rgba(255,255,255,.1);
}
*{box-sizing:border-box;margin:0;padding:0}
html,body{width:1200px;height:900px;overflow:hidden}
body{font-family:"Montserrat",sans-serif;color:var(--white);position:relative;background:var(--night-top)}
.backdrop{position:absolute;inset:0;background:
  linear-gradient(180deg,var(--night-top) 0%,var(--night-mid) 25%,var(--dusk) 48%,#b27069 66%,#5b3f6e 78%,var(--ground) 100%)}
.sidebar{position:absolute;left:0;top:0;width:121px;height:900px;background:var(--sidebar)}
.nav-item{position:absolute;left:0;width:121px;text-align:center;font-size:15px;font-weight:500}
.nav-item svg{display:block;margin:0 auto 10px;width:54px;height:54px}
.topbar-line{position:absolute;left:121px;right:0;top:91px;border-top:1px solid rgba(255,255,255,.12)}
.search{position:absolute;left:141px;top:18px;width:586px;height:52px;border-radius:26px;background:var(--search);font-size:15px;color:rgba(255,255,255,.75);padding:16px 32px}
.search svg{position:absolute;right:26px;top:17px}
.icon-btn{position:absolute;top:25px;width:40px;height:40px;border-radius:50%;background:rgba(255,255,255,.12)}
.icon-btn svg{position:absolute;left:10px;top:10px}
.icon-btn .dot{position:absolute;right:2px;top:3px;width:8px;height:8px;border-radius:50%;background:var(--white)}
.avatar{position:absolute;left:968px;top:18px;width:54px;height:54px;border-radius:50%;border:2px solid var(--white);background:linear-gradient(160deg,#c49a7a,#5a4638)}
.user-name{position:absolute;left:1043px;top:34px;font-size:20px;font-weight:700}
.panel-title{font-weight:900;font-size:29px;letter-spacing:.3px}
.invoices{position:absolute;left:145px;top:159px;width:648px;height:477px;border:2px solid var(--white);background:var(--invoice-body);overflow:hidden}
.invoices .photo{position:absolute;inset:0;background:radial-gradient(ellipse at 60% 60%,rgba(120,100,160,.35),transp 60%),linear-gradient(120deg,rgba(60,50,130,.2),rgba(110,90,140,.35))}
.invoices .head{position:relative;height:68px;background:var(--magenta);padding:18px 28px}
.invoice-table{position:relative;width:100%;border-collapse:collapse}
.invoice-table th{font-weight:500;font-size:17px;height:68px;text-align:left;border-bottom:1px solid var(--row-line)}
.invoice-table td{font-size:15px;height:75px;border-bottom:1px solid var(--row-line)}
.invoice-table th:first-child,.invoice-table td:first-child{padding-left:32px;width:220px}
.c-amount{width:157px}.c-date{width:151px}
.todo{position:absolute;left:817px;top:158px;width:356px;height:478px;border:2px solid var(--white);background:linear-gradient(180deg,var(--todo-top),var(--todo-bottom));overflow:hidden}
.todo .head{height:70px;background:linear-gradient(90deg,#7fd7b4,#a8e6c8);padding:20px 24px}
.timeline{position:absolute;left:38px;top:120px;width:6px;height:292px;background:var(--white)}
.task{position:absolute;left:28px}
.task .dot{position:absolute;left:0;top:0;width:24px;height:24px;border-radius:50%;background:var(--white)}
.task .when{position:absolute;left:42px;top:2px;font-size:16px;font-weight:700;white-space:nowrap}
.task .what{position:absolute;left:42px;top:26px;font-size:14px;font-weight:600;white-space:nowrap}
.stats{position:absolute;left:145px;top:664px;width:1028px;height:170px;border:2px solid var(--muted-orange);background:linear-gradient(180deg,var(--stats-top),var(--stats-bottom))}
.stats .panel-title{position:absolute;left:30px;top:32px}
.tab{position:absolute;top:91px;height:44px;line-height:40px;font-size:17px;text-align:center;border-radius:22px}
.tab.active{border:2px solid var(--white)}
.tab.dim{color:var(--muted-orange)}
.tab.filled{background:var(--pill)}
</style>
</head>
<body>
<div class="backdrop" role="img" aria-label="Background photograph of a starry night sky over a mountain landscape at dusk"></div>

<nav class="sidebar">
  <div class="nav-item" style="top:40px">
    <svg viewBox="0 0 54 54" fill="none" stroke="#fff" stroke-width="2"><circle cx="27" cy="27" r="21"/><circle cx="27" cy="27" r="16"/><path d="M27 33 L33 19"/><path d="M18 40 h18"/></svg>Dashboard</div>
  <div class="nav-item" style="top:162px">
    <svg viewBox="0 0 54 54" fill="none" stroke="#9fb8dc" stroke-width="2"><path d="M12 4h22l10 10v36H12z"/><path d="M34 4v10h10"/><path d="M18 22h20M18 28h20M18 34h20M18 40h14"/></svg>Invoices</div>
  <div class="nav-item" style="top:284px">
    <svg viewBox="0 0 54 54" fill="none" stroke="#fff" stroke-width="2"><circle cx="27" cy="18" r="10"/><path d="M10 48c0-12 8-18 17-18s17 6 17 18z"/></svg>Contacts</div>
  <div class="nav-item" style="top:406px">
    <svg viewBox="0 0 54 54" fill="none" stroke="#fff" stroke-width="2"><path d="M4 10h8l6 24h26l5-18H15"/><circle cx="22" cy="42" r="3"/><circle cx="40" cy="42" r="3"/></svg>Products</div>
  <div class="nav-item" style="top:528px">
    <svg viewBox="0 0 54 54" fill="none" stroke="#fff" stroke-width="2"><path d="M6 18 27 6l21 12z"/><path d="M10 18v4h34v-4M14 24v16M23 24v16M31 24v16M40 24v16M8 42h38v5H8z"/></svg>Banking</div>
  <div class="nav-item" style="top:646px">
    <svg viewBox="0 0 54 54" fill="none" stroke="#fff" stroke-width="2"><ellipse cx="20" cy="8" rx="14" ry="4"/><path d="M6 8v8c0 2 6 4 14 4M6 16v8c0 2 6 4 10 4M6 24v8c0 2 6 4 10 4M6 32v8c0 2 6 4 12 4"/><circle cx="34" cy="36" r="13"/><path d="M38 30c-2-2-9-2-8 2s9 2 8 6-7 3-9 1M34 26v20"/></svg>Expenses</div>
  <div class="nav-item" style="top:768px">
    <svg viewBox="0 0 54 54" fill="none" stroke="#fff" stroke-width="2"><circle cx="8" cy="38" r="4"/><circle cx="20" cy="24" r="4"/><circle cx="32" cy="36" r="4"/><circle cx="46" cy="18" r="4"/><path d="M11 35l6-8M23 27l6 6M35 33l8-12"/></svg>Reports</div>
</nav>

<div class="search">Search
  <svg width="18" height="18" viewBox="0 0 18 18" fill="none" stroke="#fff" stroke-width="2"><circle cx="7.5" cy="7.5" r="5.5"/><path d="M11.5 11.5 16 16"/></svg>
</div>
<div class="icon-btn" style="left:830px">
  <svg width="20" height="20" viewBox="0 0 20 20" fill="#fff"><path d="M10 1c-4 0-6 3-6 6v5l-2 3h16l-2-3V7c0-3-2-6-6-6z"/><circle cx="10" cy="17" r="2.5"/></svg><span class="dot"></span></div>
<div class="icon-btn" style="left:895px">
  <svg width="20" height="20" viewBox="0 0 20 20" fill="#fff"><path d="M1 4h18v12H1z"/><path d="M1 4l9 7 9-7" stroke="#3a2a66" stroke-width="1.8" fill="none"/></svg><span class="dot"></span></div>
<div class="avatar" role="img" aria-label="User profile photo"></div>
<div class="user-name">MARK DAVEN</div>
<div class="topbar-line"></div>

<section class="invoices">
  <div class="photo" role="img" aria-label="Background photo of a person working at a laptop"></div>
  <div class="head"><h2 class="panel-title">INVOICES</h2></div>
  <table class="invoice-table">
    <thead><tr><th>Customers</th><th class="c-amount">Amount</th><th class="c-date">Date</th><th>Due Date</th></tr></thead>
    <tbody>
      <tr><td>Lena Marsh</td><td>$ 264.00</td><td>17:09:2018</td><td>25:09:2018</td></tr>
      <tr><td>Lena Marsh</td><td>$ 264.00</td><td>17:09:2018</td><td>25:09:2018</td></tr>
      <tr><td>Lena Marsh</td><td>$ 264.00</td><td>17:09:2018</td><td>25:09:2018</td></tr>
      <tr><td>Lena Marsh</td><td>$ 264.00</td><td>17:09:2018</td><td>25:09:2018</td></tr>
    </tbody>
  </table>
</section>

<section class="todo">
  <div class="head"><h2 class="panel-title">TO-DO LIST</h2></div>
  <div class="timeline"></div>
  <div class="task" style="top:108px"><span class="dot"></span><div class="when">TODAY 14 -20</div><div class="what">Lorem Ipsum is simply dummy text</div></div>
  <div class="task" style="top:205px"><span class="dot"></span><div class="when">TODAY 14 -20</div><div class="what">Lorem Ipsum is simply dummy text</div></div>
  <div class="task" style="top:301px"><span class="dot"></span><div class="when">TODAY 14 -20</div><div class="what">Lorem Ipsum is simply dummy text</div></div>
  <div class="task" style="top:398px"><span class="dot"></span><div class="when">TODAY 14 -20</div><div class="what">Lorem Ipsum is simply dummy text</div></div>
</section>

<section class="stats">
  <h2 class="panel-title">STATISTICS</h2>
  <div class="tab active" style="left:31px;width:107px">Year</div>
  <div class="tab dim" style="left:150px;width:94px">Month</div>
  <div class="tab dim" style="left:262px;width:94px">Week</div>
  <div class="tab filled" style="left:780px;width:109px">Income</div>
  <div class="tab" style="left:902px;width:100px">Expenses</div>
</section>
</body>
</html>
```